Kestrel Roofpower Company need Flier for Bureau of Fuel Planning

We need a 2 page flier for distributing to Military Contractors and Bureau of Fuel Planning. We install residential solar and this will be used for military base housing and other gov. projects on the residential home communities. We need to show how large of a company we are and how we are able to work with the military //gov. projects. Attached is our website and other marketing info for your use. Thanks and good luck!

Target Market(s)

Military and Government Contractors //Bureau of Fuel Planning

Industry/Entity Type

Solar Energy

Requirements
Must have
• Our Why - Statement included

```html
<!DOCTYPE html>
<html lang="en">
<head>
<meta charset="utf-8">
<title>Kestrel Roofpower – Rack Card</title>
<link href="https://fonts.googleapis.com/css2?family=Lato:wght@400;700;900&display=swap" rel="stylesheet">
<style>
:root{
  --navy:#1b2f6e;
  --blue:#1f86d1;
  --blue-deep:#1660b0;
  --green:#8cc63f;
  --ink:#3d3d3d;
  --grey:#5a5a5a;
  --page:#e9e9e9;
  --white:#ffffff;
}
*{margin:0;padding:0;box-sizing:border-box}
html,body{width:1200px;height:1079px;overflow:hidden;background:var(--page);font-family:'Lato',sans-serif}
.card{position:absolute;top:90px;width:430px;height:900px;background:var(--white);overflow:hidden;box-shadow:0 4px 14px rgba(0,0,0,.18)}
.card--front{left:125px}
.card--back{left:645px}
.card svg.card__art{position:absolute;left:0;top:0;width:430px;height:900px}
.t{position:absolute;left:0;width:100%;text-align:center}
.headline{font-weight:900;color:var(--white);font-size:29px;top:26px;letter-spacing:.3px}
.headline--green{color:var(--green);font-size:46px;top:58px}
.brand-name{font-weight:700;color:var(--blue);font-size:29px;letter-spacing:.5px}
.points{position:absolute;left:0;width:100%}
.point{position:absolute;left:98px;width:300px;font-size:15px;line-height:19px;color:var(--ink)}
.point b{color:var(--blue);font-weight:900}
.cta{font-weight:900;color:var(--green);font-size:12.5px;top:793px}
.phone{position:absolute;top:819px;left:118px;width:194px;height:23px;border-radius:12px;background:var(--green);color:var(--navy);font-weight:900;font-size:12px;display:flex;align-items:center;justify-content:center;gap:6px}
.web{font-weight:900;color:var(--white);font-size:12.5px;top:848px}
.addr{color:var(--white);font-size:12px;top:870px}
.reviews-title{color:var(--white);font-size:15px;top:22px;letter-spacing:.2px}
.quote{position:absolute;left:62px;width:352px;color:var(--white);font-size:12px;line-height:16px}
.quote span{color:var(--green);display:block}
.qmark{position:absolute;left:18px;color:var(--green);font-weight:900;font-size:54px;line-height:1}
.welcome{color:var(--grey);font-weight:700;font-size:18px}
.step{position:absolute;width:100px;text-align:center;top:480px}
.step h3{font-size:8px;font-weight:700;color:var(--ink);line-height:11px;text-transform:uppercase}
.step p{font-size:7.5px;color:var(--grey);line-height:10px;margin-top:10px}
.switch{color:var(--white);font-weight:900;font-size:28px;line-height:38px;top:642px}
</style>
</head>
<body>

<section class="card card--front">
  <svg class="card__art" viewBox="0 0 430 900" aria-hidden="false">
    <defs>
      <linearGradient id="heroFill" x1="0" y1="0" x2="0" y2="1">
        <stop offset="0" stop-color="#1c2f6c"/>
        <stop offset=".35" stop-color="#4d6690"/>
        <stop offset=".7" stop-color="#8c9a8a"/>
        <stop offset="1" stop-color="#4e6b3a"/>
      </linearGradient>
      <linearGradient id="roofFill" x1="0" y1="0" x2="0" y2="1">
        <stop offset="0" stop-color="#ffffff"/>
        <stop offset=".4" stop-color="#e7eaee"/>
        <stop offset="1" stop-color="#f2f3f4"/>
      </linearGradient>
      <linearGradient id="bandFill" x1="0" y1="0" x2="0" y2="1">
        <stop offset="0" stop-color="#2a8fd6"/>
        <stop offset="1" stop-color="#1660b0"/>
      </linearGradient>
    </defs>
    <rect x="0" y="500" width="430" height="280" fill="url(#roofFill)" role="img" aria-label="Faded photo of a house roof with solar panels"/>
    <path d="M0 0H430V320Q215 450 0 320Z" fill="url(#heroFill)" role="img" aria-label="Photo of a military family standing in front of a two-storey house with rooftop solar panels"/>
    <path d="M0 320Q215 450 430 320" fill="none" stroke="var(--green)" stroke-width="6"/>
    <circle cx="215" cy="378" r="64" fill="var(--white)" stroke="var(--blue)" stroke-width="8"/>
    <line x1="42" y1="542" x2="388" y2="542" stroke="var(--blue-deep)" stroke-width="2"/>
    <line x1="42" y1="610" x2="388" y2="610" stroke="var(--blue-deep)" stroke-width="2"/>
    <line x1="42" y1="678" x2="388" y2="678" stroke="var(--blue-deep)" stroke-width="2"/>
    <g fill="var(--green)">
      <circle cx="59" cy="576" r="22"/>
      <circle cx="59" cy="645" r="22"/>
      <circle cx="59" cy="713" r="22"/>
    </g>
    <circle cx="59" cy="576" r="11" fill="none" stroke="var(--white)" stroke-width="3"/>
    <g stroke="var(--white)" stroke-width="2.5">
      <circle cx="59" cy="645" r="6" fill="var(--white)"/>
      <line x1="59" y1="630" x2="59" y2="634"/><line x1="59" y1="656" x2="59" y2="660"/>
      <line x1="44" y1="645" x2="48" y2="645"/><line x1="70" y1="645" x2="74" y2="645"/>
      <line x1="48" y1="634" x2="51" y2="637"/><line x1="67" y1="653" x2="70" y2="656"/>
      <line x1="70" y1="634" x2="67" y2="637"/><line x1="51" y1="653" x2="48" y2="656"/>
    </g>
    <text x="59" y="721" text-anchor="middle" font-family="Lato,sans-serif" font-weight="900" font-size="21" fill="var(--white)">$0</text>
    <path d="M0 792Q215 726 430 792" fill="none" stroke="var(--white)" stroke-width="10"/>
    <path d="M0 800Q215 734 430 800V900H0Z" fill="url(#bandFill)"/>
  </svg>

  <div class="t headline">SAVE THOUSANDS BY</div>
  <div class="t headline headline--green">GOING SOLAR</div>
  <div class="t brand-name" style="top:456px">KESTREL ROOFPOWER</div>

  <div class="points">
    <p class="point" style="top:558px"><b>WHY:</b> The planet and your pocket book will thank you.</p>
    <p class="point" style="top:626px"><b>HOW:</b> Bringing the power of the Sun to you.</p>
    <p class="point" style="top:696px"><b>WHAT:</b> Zero upfront cost power monthly energy costs.</p>
  </div>

  <div class="t cta">CALL TODAY FOR A NO OBLIGATION CONSULTATION</div>
  <div class="phone"><svg width="12" height="12" viewBox="0 0 24 24"><circle cx="12" cy="12" r="10.5" fill="none" stroke="var(--navy)" stroke-width="2"/><path d="M8 7c0 5 4 9 9 9l1-2-3-1-1 1c-2-1-3-2-4-4l1-1-1-3z" fill="var(--navy)"/></svg>(800) 555-0142</div>
  <div class="t web">www.kestrelroofpower.com</div>
  <div class="t addr">118 Harrow Ln., Suite 210-B, Millbrook NJ 08099</div>
</section>

<section class="card card--back">
  <svg class="card__art" viewBox="0 0 430 900">
    <defs>
      <linearGradient id="topBand" x1="0" y1="0" x2="0" y2="1">
        <stop offset="0" stop-color="#1b3a86"/>
        <stop offset="1" stop-color="#1a6cc0"/>
      </linearGradient>
      <linearGradient id="houseFade" x1="0" y1="0" x2="0" y2="1">
        <stop offset="0" stop-color="#ffffff"/>
        <stop offset=".5" stop-color="#eceef1"/>
        <stop offset="1" stop-color="#f4f5f6"/>
      </linearGradient>
      <linearGradient id="panelFill" x1="0" y1="0" x2="1" y2="1">
        <stop offset="0" stop-color="#8a6a5a"/>
        <stop offset=".35" stop-color="#2b3566"/>
        <stop offset="1" stop-color="#1d2150"/>
      </linearGradient>
      <linearGradient id="bandFill2" x1="0" y1="0" x2="0" y2="1">
        <stop offset="0" stop-color="#2a8fd6"/>
        <stop offset="1" stop-color="#1660b0"/>
      </linearGradient>
    </defs>
    <rect x="0" y="300" width="430" height="320" fill="url(#houseFade)" role="img" aria-label="Faded photo of a house with solar panels"/>
    <path d="M0 0H430V160Q215 260 0 160Z" fill="url(#topBand)"/>
    <path d="M0 166Q215 266 430 166" fill="none" stroke="var(--green)" stroke-width="6"/>
    <circle cx="215" cy="228" r="52" fill="var(--white)" stroke="var(--blue)" stroke-width="7"/>
    <g fill="var(--white)" stroke="var(--green)" stroke-width="2.5">
      <circle cx="54" cy="445" r="29"/><circle cx="161" cy="445" r="29"/>
      <circle cx="267" cy="445" r="29"/><circle cx="373" cy="445" r="29"/>
    </g>
    <g fill="none" stroke="var(--blue)" stroke-width="2">
      <rect x="42" y="434" width="24" height="18" rx="2"/>
      <rect x="149" y="433" width="24" height="17" rx="1"/><line x1="161" y1="450" x2="161" y2="457"/>
      <rect x="257" y="433" width="16" height="22" rx="1"/><circle cx="275" cy="452" r="6"/>
      <circle cx="373" cy="441" r="7"/><line x1="370" y1="451" x2="376" y2="451"/>
    </g>
    <g fill="none" stroke="var(--grey)" stroke-width="1" stroke-dasharray="2 3">
      <path d="M88 440Q108 430 128 440"/><path d="M195 440Q214 430 233 440"/><path d="M301 440Q320 430 339 440"/>
    </g>
    <path d="M0 615Q215 565 430 615V800H0Z" fill="url(#panelFill)" role="img" aria-label="Close-up photo of solar panels in sunlight"/>
    <path d="M0 792Q215 726 430 792" fill="none" stroke="var(--white)" stroke-width="10"/>
    <path d="M0 800Q215 734 430 800V900H0Z" fill="url(#bandFill2)"/>
  </svg>

  <div class="t reviews-title">WHAT PEOPLE ARE SAYING</div>
  <div class="qmark" style="top:48px">“</div>
  <p class="quote" style="top:56px">I had met with a few different companies and didn't care for their options. Kestrel had an option we liked and we went for it! Its been working great for us.<span>Dale and Rosa K.</span></p>
  <div class="qmark" style="top:122px">“</div>
  <p class="quote" style="top:130px">My husband and I decided to go solar after 3 of our neighbors did. After having it I don't know why we waited so long!<span>Megan T.</span></p>

  <div class="t brand-name" style="top:290px">KESTREL ROOFPOWER</div>
  <div class="t welcome" style="top:350px">Welcome to Kestrel Roofpower</div>
  <div class="t welcome" style="top:376px">We Make It Easy</div>

  <div class="step" style="left:4px"><h3>Speak to a solar<br>consultant</h3><p>Meet with one of our energy consultants to review your solar options.</p></div>
  <div class="step" style="left:111px"><h3>We'll design your<br>solar panel system</h3><p>We'll finalize the details for tip top accuracy.</p></div>
  <div class="step" style="left:217px"><h3>Schedule your<br>1 day install</h3><p>Let us do the heavy lifting as you watch your home upgrade to solar.</p></div>
  <div class="step" style="left:323px"><h3>Start saving on<br>your electricity bill</h3><p>Watch your electric bill lower and your energy savings build for year to come.</p></div>

  <div class="t switch">MAKE THE SWITCH<br>TO BETTER ENERGY</div>

  <div class="t cta">CALL TODAY FOR A NO OBLIGATION CONSULTATION</div>
  <div class="phone"><svg width="12" height="12" viewBox="0 0 24 24"><circle cx="12" cy="12" r="10.5" fill="none" stroke="var(--navy)" stroke-width="2"/><path d="M8 7c0 5 4 9 9 9l1-2-3-1-1 1c-2-1-3-2-4-4l1-1-1-3z" fill="var(--navy)"/></svg>(800) 555-0142</div>
  <div class="t web">www.kestrelroofpower.com</div>
  <div class="t addr">118 Harrow Ln., Suite 210-B, Millbrook NJ 08099</div>
</section>

</body>
</html>
```